Don't want to drink it?

I'm putting together an infographic to use on my website detailing the multiple uses of coffee grinds. Ive attached a picture of one i made with text descriptions regarding other use cases of coffee. The infographic needs to have a similar color theme to my website which is primarily white with secondary black and red. Playful illustrations with coffee related vectors and cartoons will be highly appreciated. I want the infographic to have a fun vibe.

```html
<!DOCTYPE html>
<html lang="en">
<head>
<meta charset="utf-8">
<title>Don't Want to Drink It? – Brookhollow Coffee</title>
<link rel="stylesheet" href="https://fonts.googleapis.com/css2?family=Anton&family=Oswald:wght@300;400;600&family=Open+Sans:wght@400;600;700&display=swap">
<style>
  :root {
    --espresso: #3a2114;
    --roast: #52301c;
    --cream: #f3efe9;
    --orange: #f49b1f;
    --orange-deep: #e0841a;
    --red: #d8261b;
    --ink: #1d1a18;
    --green: #8cbf3b;
    --green-soft: #a6d05e;
    --peach: #f6a93a;
    --peach-soft: #f9c072;
    --purple: #8a5ba8;
    --purple-soft: #a47cc0;
    --sky: #3fb1d9;
    --sky-soft: #74c7e6;
    --wood: #b8794a;
    --white: #ffffff;
  }
  * { box-sizing: border-box; margin: 0; padding: 0; }
  html, body { width: 849px; height: 1200px; overflow: hidden; }
  body { background: var(--cream); font-family: "Open Sans", sans-serif; color: var(--ink); }
  .infographic { position: relative; width: 849px; height: 1200px; overflow: hidden; }

  .top-band { position: absolute; left: 0; top: 0; width: 849px; height: 88px; background: var(--espresso); }
  .accent-band { position: absolute; left: 0; top: 88px; width: 849px; height: 14px; background: var(--orange); }
  .brand-tab {
    position: absolute; left: 306px; top: 0; width: 237px; height: 112px;
    background: var(--orange); border-radius: 0 0 10px 10px;
    display: flex; align-items: center; justify-content: center; gap: 10px;
  }
  .brand-name {
    font-family: "Oswald", sans-serif; font-weight: 600; font-size: 30px;
    color: var(--white); text-transform: uppercase; letter-spacing: 1px; line-height: 1;
  }
  .brand-dot { width: 14px; height: 14px; border-radius: 50%; background: var(--white); }

  .headline {
    position: absolute; left: 0; top: 140px; width: 849px; text-align: center;
    font-family: "Anton", sans-serif; font-size: 70px; line-height: 1; color: var(--ink);
    letter-spacing: 1px; text-transform: uppercase;
  }
  .headline .mark { color: var(--red); }

  .uses-board { position: absolute; left: 0; top: 252px; width: 849px; height: 735px; background: var(--roast); }

  .use-card { position: absolute; width: 338px; height: 300px; border-radius: 6px; padding: 22px 22px; color: var(--white); overflow: hidden; }
  .use-card h2 { font-family: "Oswald", sans-serif; text-transform: uppercase; line-height: 1; }
  .use-card .lead { font-weight: 300; font-size: 48px; display: block; }
  .use-card .key { font-weight: 400; font-size: 40px; display: block; }
  .use-card p { font-size: 16px; line-height: 1.35; margin-top: 14px; width: 190px; }
  .use-card .art { position: absolute; right: 18px; bottom: 18px; width: 110px; height: 170px; border-radius: 8px; }

  .card-fertilizer { left: 80px; top: 32px; background: var(--green); }
  .card-fertilizer .art { background: linear-gradient(180deg, var(--green-soft), #5e8f2a); }
  .card-face { left: 432px; top: 32px; background: var(--peach); }
  .card-face .art { background: linear-gradient(180deg, var(--peach-soft), var(--orange-deep)); }
  .card-insects { left: 80px; top: 352px; background: var(--purple); }
  .card-insects p { width: 290px; }
  .card-insects .art { width: 290px; height: 70px; left: 22px; right: auto; background: linear-gradient(90deg, var(--purple-soft), #6b3f88); }
  .card-sink { left: 432px; top: 352px; background: var(--sky); }
  .card-sink .art { background: linear-gradient(180deg, var(--sky-soft), #2a8db3); }
  .card-sink p { margin-top: 10px; }

  .furniture-art { position: absolute; left: 70px; top: 1010px; width: 320px; height: 170px; border-radius: 8px;
    background: linear-gradient(180deg, #c98a57, #8f5632); }
  .furniture-tip { position: absolute; left: 410px; top: 1000px; width: 400px; }
  .furniture-tip h2 { font-family: "Oswald", sans-serif; font-weight: 400; font-size: 38px; line-height: 1.05; text-transform: uppercase; color: var(--ink); }
  .furniture-tip p { font-size: 16px; line-height: 1.4; margin-top: 12px; color: var(--ink); }
</style>
</head>
<body>
<main class="infographic">
  <div class="top-band"></div>
  <div class="accent-band"></div>
  <div class="brand-tab">
    <span class="brand-dot"></span>
    <span class="brand-name">Brookhollow Coffee</span>
  </div>

  <h1 class="headline">Don't want to drink it<span class="mark">?</span></h1>

  <section class="uses-board">
    <article class="use-card card-fertilizer">
      <h2><span class="lead">Use it as</span><span class="key">Fertilizer</span></h2>
      <p>Use your coffee grounds as an organic fertilizer without the bad smell! It's a good source of nitrogen, calcium and magnesium</p>
      <div class="art" role="img" aria-label="Potted plants with a garden trowel"></div>
    </article>

    <article class="use-card card-face">
      <h2><span class="lead">Clean your</span><span class="key">Face!</span></h2>
      <p>Mix coffee grinds with some coconut oil to make homemade exfoliating cream!</p>
      <div class="art" role="img" aria-label="Illustration of a woman applying face scrub"></div>
    </article>

    <article class="use-card card-insects">
      <h2><span class="lead">Keep those</span><span class="key">Insects away</span></h2>
      <p>By sprinkling coffee grounds where insects frequent, you can save on the cost of bug spray!</p>
      <div class="art" role="img" aria-label="Row of crawling insects"></div>
    </article>

    <article class="use-card card-sink">
      <h2><span class="lead">Unclog</span><span class="key">Your sink</span></h2>
      <p>Mix some coffee grinds with dish-washing detergent and hot water to make quick work of that grease buildup in your pipes!</p>
      <div class="art" role="img" aria-label="Bathroom sink with faucet"></div>
    </article>
  </section>

  <div class="furniture-art" role="img" aria-label="Wooden table"></div>
  <section class="furniture-tip">
    <h2>Cover scratches on wooden furniture</h2>
    <p>Have scratches on your wooden furniture? Rub some coffee paste to give it back its natural shine by mixing coffee grounds with some hot water.</p>
  </section>
</main>
</body>
</html>
```